Business card

Looking for modern clean business card off logo below. Very important to be clean and professional but want fun as well

Industry/Entity Type

Business

```html
<!DOCTYPE html>
<html lang="en">
<head>
<meta charset="utf-8">
<title>Summit Estates – Business Card</title>
<link rel="stylesheet" href="https://fonts.googleapis.com/css2?family=Open+Sans:wght@400;600;700&display=swap">
<style>
  :root {
    --page-bg: #d9dbdd;
    --card-white: #f7f7f5;
    --brand-blue: #4fb3cc;
    --brand-blue-soft: #7ccadc;
    --charcoal: #4a4a4c;
    --text-dark: #4d4d4f;
    --text-muted: #6d6d70;
  }
  * { box-sizing: border-box; margin: 0; padding: 0; }
  html, body { width: 1200px; height: 968px; overflow: hidden; }
  body {
    background: var(--page-bg);
    font-family: "Open Sans", Arial, sans-serif;
    position: relative;
  }
  .card {
    position: absolute;
    background: var(--card-white);
    overflow: hidden;
    box-shadow: 0 2px 6px rgba(0,0,0,0.12);
  }

  /* Front face */
  .card-front { left: 580px; top: 80px; width: 540px; height: 309px; }
  .front-top-band {
    position: absolute; left: 0; top: 0; width: 100%; height: 58px;
    background: var(--brand-blue);
  }
  .front-mid-band {
    position: absolute; left: 0; top: 70px; width: 100%; height: 10px;
    background: var(--brand-blue-soft);
  }
  .front-base {
    position: absolute; left: 0; bottom: 0; width: 100%; height: 150px;
    background: var(--charcoal);
  }
  .front-brand {
    position: absolute; left: 36px; bottom: 56px;
    display: flex; align-items: center; gap: 14px;
  }
  .brand-dot {
    width: 34px; height: 34px; border-radius: 50%;
    background: var(--card-white);
  }
  .front-brand .brand-name {
    color: var(--card-white); font-weight: 700; font-size: 34px; letter-spacing: 1px;
  }
  .front-tagline {
    position: absolute; left: 84px; bottom: 36px;
    color: var(--card-white); font-size: 12px; letter-spacing: 0.3px;
  }

  /* Contact face */
  .card-contact { left: 80px; top: 520px; width: 600px; height: 343px; }
  .contact-mark {
    position: absolute; left: 40px; top: 36px;
    width: 58px; height: 58px; border-radius: 50%;
    background: var(--brand-blue);
  }
  .holder {
    position: absolute; right: 40px; top: 36px; text-align: right;
  }
  .holder-name { color: var(--brand-blue); font-weight: 700; font-size: 17px; letter-spacing: 0.5px; }
  .holder-role { color: var(--text-dark); font-size: 12px; }
  .company-block {
    position: absolute; left: 40px; top: 150px;
    color: var(--text-dark); font-size: 14px; line-height: 18px;
  }
  .company-block .brand-name { color: var(--brand-blue); font-weight: 700; font-size: 15px; letter-spacing: 0.5px; }
  .contact-list {
    position: absolute; left: 40px; top: 238px;
    list-style: none; color: var(--text-dark); font-size: 14px; line-height: 18px;
  }
  .contact-list li { display: flex; align-items: center; gap: 10px; }
  .contact-list svg { width: 13px; height: 13px; fill: var(--text-muted); flex: none; }
  .website {
    position: absolute; right: 40px; bottom: 50px;
    color: var(--text-dark); font-size: 14px;
  }
  .website strong { color: var(--brand-blue); font-weight: 600; }
</style>
</head>
<body>

<section class="card card-front" aria-label="Card front">
  <div class="front-top-band"></div>
  <div class="front-mid-band"></div>
  <div class="front-base"></div>
  <div class="front-brand">
    <span class="brand-dot"></span>
    <span class="brand-name">SUMMIT ESTATES</span>
  </div>
  <p class="front-tagline">Property Management and Real Estate</p>
</section>

<section class="card card-contact" aria-label="Card back">
  <span class="contact-mark"></span>
  <div class="holder">
    <p class="holder-name">ALEX MORGAN</p>
    <p class="holder-role">Director</p>
  </div>
  <div class="company-block">
    <p class="brand-name">SUMMIT ESTATES</p>
    <p>12 Harbour Lane</p>
    <p>Westbrook VIC 3190</p>
    <p>Melbourne</p>
  </div>
  <ul class="contact-list">
    <li><svg viewBox="0 0 12 12"><rect x="3" y="0" width="6" height="12" rx="1"/></svg>+00 (0)987 654 321</li>
    <li><svg viewBox="0 0 12 12"><path d="M2 1h3l1 3-2 1a7 7 0 0 0 3 3l1-2 3 1v3c0 1-1 1-1 1A10 10 0 0 1 1 2s0-1 1-1z"/></svg>+00 (0)987 654 321</li>
    <li><svg viewBox="0 0 12 12"><rect x="1" y="5" width="10" height="6" rx="1"/><rect x="3" y="1" width="6" height="4"/></svg>+00 (0)987 654 321</li>
    <li><svg viewBox="0 0 12 12"><path d="M0 2h12v8H0z M1 3l5 4 5-4" fill="none" stroke="#6d6d70" stroke-width="1.2"/></svg>hello@summitestates.com</li>
  </ul>
  <p class="website">www.<strong>summitestates</strong>.com</p>
</section>

</body>
</html>
```